Real Estate Investing company needs a business card design

We need a business card design for new Real Estate Investment Company called "Maple Ridge Ventures, LLC." We buy homes for cash and close quickly in any situation. Our company provides an easy and fast option for home owners who are in tough situations who need to sell their home fast and don't want realtor fees or other listing hassles. We also renovate and resell our homes which helps provide housing for the community. We would like to see designs that use the colors blue and white to match our company logo or other colors that may match our company logo. The final design should communicate trust and easy process.
Industry/Entity Type
Business
Contact Information for Business Card
Front should have company name and company logo. back of card should have company logo and area to list services.
Look and feel

```html
<!DOCTYPE html>
<html lang="en">
<head>
<meta charset="utf-8">
<title>Maple Ridge Ventures, LLC – Business Card</title>
<link href="https://fonts.googleapis.com/css2?family=Arimo:wght@400;700&display=swap" rel="stylesheet">
<style>
  :root {
    --page-bg: #e4e5e7;
    --brand-blue: #0f5fb3;
    --ink-blue: #0d3f86;
    --text-blue: #1b5cae;
    --card-white: #ffffff;
    --card-shadow: rgba(0, 0, 0, 0.18);
  }
  * { margin: 0; padding: 0; box-sizing: border-box; }
  html, body {
    width: 1200px;
    height: 900px;
    overflow: hidden;
    background: var(--page-bg);
    font-family: "Arimo", Arial, sans-serif;
  }
  .canvas {
    position: relative;
    width: 1200px;
    height: 900px;
  }
  .card {
    position: absolute;
    width: 640px;
    height: 366px;
    border-radius: 4px;
    box-shadow: 0 6px 18px var(--card-shadow);
  }

  /* Back of card */
  .card-back {
    left: 470px;
    top: 80px;
    background: var(--brand-blue);
    color: var(--card-white);
  }
  .services {
    position: absolute;
    left: 40px;
    top: 34px;
  }
  .services-title {
    font-size: 17px;
    font-weight: 400;
    letter-spacing: 0.5px;
    margin-bottom: 6px;
  }
  .services-list {
    list-style: none;
  }
  .services-list li {
    font-size: 14px;
    line-height: 18px;
    padding-left: 14px;
    position: relative;
  }
  .services-list li::before {
    content: "";
    position: absolute;
    left: 2px;
    top: 6px;
    width: 6px;
    height: 6px;
    border-radius: 50%;
    background: var(--card-white);
  }
  .brand-back {
    position: absolute;
    right: 40px;
    bottom: 50px;
    display: flex;
    align-items: center;
    gap: 12px;
  }
  .brand-back .brand-mark {
    width: 18px;
    height: 18px;
    background: var(--card-white);
  }
  .brand-back .brand-name {
    font-size: 26px;
    font-weight: 700;
    color: var(--card-white);
  }

  /* Front of card */
  .card-front {
    left: 90px;
    top: 440px;
    background: var(--card-white);
  }
  .brand-front {
    position: absolute;
    left: 36px;
    top: 150px;
    width: 250px;
    display: flex;
    align-items: center;
    gap: 10px;
  }
  .brand-front .brand-mark {
    flex: none;
    width: 16px;
    height: 16px;
    background: var(--brand-blue);
  }
  .brand-front .brand-name {
    font-size: 22px;
    font-weight: 700;
    line-height: 1.2;
    color: var(--brand-blue);
  }
  .divider {
    position: absolute;
    left: 316px;
    top: 100px;
    width: 2px;
    height: 166px;
    background: var(--brand-blue);
  }
  .contact {
    position: absolute;
    left: 342px;
    top: 120px;
    color: var(--text-blue);
  }
  .contact-name {
    font-size: 24px;
    font-weight: 700;
    color: var(--ink-blue);
  }
  .contact-title {
    font-size: 16px;
    margin-top: 2px;
    margin-bottom: 18px;
  }
  .contact-line {
    font-size: 17px;
    line-height: 22px;
  }
</style>
</head>
<body>
<main class="canvas">

  <section class="card card-back" aria-label="Back of business card">
    <div class="services">
      <h2 class="services-title">SERVICES</h2>
      <ul class="services-list">
        <li>Service 1</li>
        <li>Service 2</li>
        <li>Service 3</li>
        <li>Service 4</li>
        <li>Service 5</li>
      </ul>
    </div>
    <div class="brand-back">
      <span class="brand-mark" aria-hidden="true"></span>
      <span class="brand-name">Maple Ridge Ventures, LLC</span>
    </div>
  </section>

  <section class="card card-front" aria-label="Front of business card">
    <div class="brand-front">
      <span class="brand-mark" aria-hidden="true"></span>
      <span class="brand-name">Maple Ridge Ventures, LLC</span>
    </div>
    <div class="divider" aria-hidden="true"></div>
    <div class="contact">
      <p class="contact-name">Your name here</p>
      <p class="contact-title">Title here</p>
      <p class="contact-line">Tel: 0555-0147-2093</p>
      <p class="contact-line">Email: info@mapleridgevc.com</p>
    </div>
  </section>

</main>
</body>
</html>
```